Hydroponic Farm Needs a Business Card

We need a business card design for a hydroponic farm located on the Gulf Coast called 'Mossbrook Farms'. We grow many forms of lettuce and tomatoes along with other herbs and spices. We currently sell to farmer's markets though will soon be expanding to commercial accounts such as restaurants and grocery stores. The colors should be bright and vibrant to reflect the nature of our produce. The final design should communicate a professional, clean, yet friendly impression and able to be used both with farmer's markets and commercial accounts.

The pictures are an example of our product. The pictures do not have to be incorporated into the business card design.

Please put areas for information such as Names, Phone Number, E-mail address, and additional information.

Farm

```html
<!DOCTYPE html>
<html lang="en">
<head>
<meta charset="utf-8">
<title>Mossbrook Farms – Business Card</title>
<link rel="stylesheet" href="https://fonts.googleapis.com/css2?family=Ubuntu:wght@400&family=Tinos&family=Oswald:wght@700&family=Kalam&display=swap">
<style>
  :root {
    --backdrop: #65524f;
    --card: #e7e2dd;
    --ink-dark: #2c2220;
    --brand-red: #6b1512;
    --leaf-green: #6aa84f;
    --leaf-pale: #b9cf9f;
    --tomato-yellow: #f7c21b;
    --tomato-pink: #e8245a;
    --tomato-orange: #f2781e;
    --tomato-green: #74b845;
    --tomato-purple: #7c2c7e;
    --tomato-red: #e52a2a;
  }
  html, body {
    margin: 0;
    width: 1200px;
    height: 1000px;
    overflow: hidden;
    background: var(--backdrop);
  }
  .canvas {
    position: relative;
    width: 1200px;
    height: 1000px;
  }
  .card {
    position: absolute;
    width: 540px;
    height: 310px;
    background: var(--card);
    box-shadow: 0 6px 14px rgba(0,0,0,0.35);
  }
  /* Contact side */
  .card--contact { left: 70px; top: 170px; }
  .contact__name {
    position: absolute;
    left: 50px;
    top: 70px;
    margin: 0;
    font-family: "Ubuntu", sans-serif;
    font-weight: 400;
    font-size: 22px;
    color: var(--ink-dark);
    letter-spacing: 0.5px;
    white-space: nowrap;
  }
  .contact__list {
    position: absolute;
    left: 54px;
    top: 112px;
    margin: 0;
    padding: 0;
    list-style: none;
    font-family: "Tinos", serif;
    font-size: 17px;
    color: #111;
  }
  .contact__item {
    display: flex;
    align-items: center;
    gap: 9px;
    height: 23px;
    white-space: nowrap;
  }
  .contact__icon { width: 15px; height: 15px; flex: none; }
  .contact__art {
    position: absolute;
    right: 22px;
    bottom: 40px;
    width: 196px;
    height: 210px;
  }
  /* Brand side */
  .card--brand { left: 600px; top: 500px; }
  .brand__name {
    position: absolute;
    right: 34px;
    top: 28px;
    margin: 0;
    display: flex;
    align-items: center;
    gap: 12px;
    font-family: "Oswald", sans-serif;
    font-weight: 700;
    font-size: 34px;
    letter-spacing: 1px;
    text-transform: uppercase;
    color: var(--brand-red);
  }
  .brand__mark {
    width: 18px;
    height: 18px;
    background: var(--brand-red);
  }
  .brand__art {
    position: absolute;
    left: 34px;
    top: 92px;
    width: 472px;
    height: 150px;
  }
  .brand__tagline {
    position: absolute;
    left: 34px;
    bottom: 20px;
    margin: 0;
    font-family: "Kalam", cursive;
    font-size: 20px;
    color: #2a2a2a;
  }
</style>
</head>
<body>
<main class="canvas">

  <section class="card card--contact">
    <h2 class="contact__name">Firstname Lastname</h2>
    <ul class="contact__list">
      <li class="contact__item">
        <svg class="contact__icon" viewBox="0 0 16 16" aria-hidden="true">
          <path d="M2 6 Q8 1 14 6 L12 8 L10 6.5 L6 6.5 L4 8 Z" fill="var(--leaf-green)"/>
          <rect x="4" y="8" width="8" height="6" rx="1" fill="var(--leaf-green)"/>
        </svg>
        <span>055-0140287</span>
      </li>
      <li class="contact__item">
        <svg class="contact__icon" viewBox="0 0 16 16" aria-hidden="true">
          <rect x="1" y="3.5" width="14" height="9" fill="none" stroke="var(--leaf-green)" stroke-width="1.4"/>
          <path d="M1 3.5 L8 9 L15 3.5" fill="none" stroke="var(--leaf-green)" stroke-width="1.4"/>
        </svg>
        <span>hello@mossbrookfarms.com</span>
      </li>
      <li class="contact__item">
        <svg class="contact__icon" viewBox="0 0 16 16" aria-hidden="true">
          <circle cx="8" cy="8" r="7" fill="var(--leaf-green)"/>
          <path d="M1 8 H15 M8 1 V15 M3 4 H13 M3 12 H13" stroke="#fff" stroke-width="0.8" fill="none"/>
        </svg>
        <span>www.mossbrookfarms.com</span>
      </li>
    </ul>
    <div class="contact__art" role="img" aria-label="Illustration of a row of colourful heirloom tomatoes beneath pale green leafy swirls"
         style="background:
           linear-gradient(90deg, var(--tomato-yellow), var(--tomato-pink) 25%, var(--tomato-orange) 45%, var(--tomato-green) 60%, var(--tomato-purple) 75%, var(--tomato-red) 90%) bottom / 100% 34% no-repeat,
           linear-gradient(180deg, rgba(185,207,159,0) 0%, var(--leaf-pale) 100%) top / 100% 66% no-repeat;
           border-radius: 14px 14px 30px 30px;"></div>
  </section>

  <section class="card card--brand">
    <h1 class="brand__name"><span class="brand__mark" aria-hidden="true"></span>Mossbrook Farms</h1>
    <div class="brand__art" role="img" aria-label="Illustration of a diagonal row of yellow, pink, orange, green, purple and red tomatoes with green stems"
         style="background: linear-gradient(100deg, var(--tomato-yellow) 0%, var(--tomato-pink) 20%, var(--tomato-orange) 38%, var(--tomato-green) 55%, var(--tomato-purple) 70%, var(--tomato-red) 85%, var(--tomato-orange) 100%);
           border-radius: 70px;"></div>
    <p class="brand__tagline">Here we grow many forms of lettuce and tomatoes</p>
  </section>

</main>
</body>
</html>
```